Buch-Cover für Berater, Coach und Trainer
Ich habe das erste Mal Ihre Leistung in Anspruch genommen und bin restlos zufrieden. Schön, wenn sich die Entscheidung für einen bestimmten Designer, auch hinterher als absolut richtig herausstellt. Es hätte nicht besser laufen können mit tv studio. Vielen Dank nochmals für die gute Kommunikation und Ihre professionellen Vorschläge.
Zielgruppe
Guten Tag,
ich bin Berater, Coach und Trainer und es geht um die Vermarktung meines (Sach-)Buches 'Deal Sprints'.
Titel des Buches:
Deal Sprints
Untertitel:
Der Schub für Ihre Verhandlungsstärke
Zielgruppe:
Verkäufer oder Menschen, die andere für ihre Ideen gewinnen möchten
Bitte melden Sie sich gerne bei Fragen.
Herzliche Grüße
Torsten Wehmeyer
Aufgabenstellung
Das das Buch recht modern geschrieben ist, sollte der Stil schon auch dem Inhalt entsprechen.
Der Titel muss kein Bild haben, gerne auch eine Illustration oder nur Text.
Als Dateiupload lege ich Ihnen den Klappentext bei.

```html
<!DOCTYPE html>
<html lang="de">
<head>
<meta charset="utf-8">
<title>Deal Sprints – Buchumschlag</title>
<link rel="stylesheet" href="https://fonts.googleapis.com/css2?family=Barlow:wght@400;500;700&family=Barlow+Semi+Condensed:wght@400;500&display=swap">
<style>
  :root {
    --page: #ffffff;
    --cover-blue: #009fe3;
    --spine-blue: #5bc5f2;
    --ink: #ffffff;
  }
  html, body {
    margin: 0;
    padding: 0;
    width: 1200px;
    height: 849px;
    overflow: hidden;
    background: var(--page);
    font-family: "Barlow", "Helvetica Neue", Arial, sans-serif;
  }
  .canvas {
    position: relative;
    width: 1200px;
    height: 849px;
  }
  .back-cover {
    position: absolute;
    left: 162px;
    top: 126px;
    width: 423px;
    height: 601px;
    background: var(--cover-blue);
    color: var(--ink);
  }
  .back-title {
    position: absolute;
    left: 29px;
    top: 62px;
    margin: 0;
    font-size: 29px;
    font-weight: 700;
    letter-spacing: 1.2px;
    line-height: 1;
  }
  .blurb {
    position: absolute;
    left: 29px;
    top: 97px;
    width: 380px;
    font-family: "Barlow Semi Condensed", "Barlow", Arial, sans-serif;
    font-size: 11.4px;
    line-height: 15.15px;
    font-weight: 500;
    letter-spacing: 0.25px;
  }
  .blurb p { margin: 0 0 15.15px; }
  .blurb .line { display: block; white-space: nowrap; }
  .spine {
    position: absolute;
    left: 585px;
    top: 126px;
    width: 55px;
    height: 601px;
    background: var(--spine-blue);
  }
  .front-cover {
    position: absolute;
    left: 640px;
    top: 126px;
    width: 425px;
    height: 601px;
    background: var(--cover-blue);
  }
  .front-cover svg, .spine svg { display: block; }
  .cover-art {
    position: absolute;
    left: 70px;
    top: 320px;
    width: 272px;
    height: 211px;
    background: var(--ink);
    border-radius: 40px 40px 90px 90px;
  }
  .front-author {
    position: absolute;
    left: 0;
    top: 561px;
    width: 100%;
    margin: 0;
    text-align: center;
    color: var(--ink);
    font-size: 21px;
    font-weight: 400;
    letter-spacing: 0.4px;
    line-height: 1;
  }
</style>
</head>
<body>
<div class="canvas">

  <section class="back-cover">
    <h2 class="back-title">DEAL SPRINTS</h2>
    <div class="blurb">
      <p>
        <span class="line">Lorem ipsum dolor sit amet, consectetuer adipiscing elit, sed diam nonum-</span>
        <span class="line">my nibh euismod tincidunt ut laoreet dolore magna aliquam erat volutpat. Ut</span>
        <span class="line">wisi enim ad minim veniam, quis nostrud exerci tation ullamcorper suscipit</span>
        <span class="line">lobortis nisl ut aliquip ex ea commodo consequat. Duis autem vel eum iriure</span>
        <span class="line">dolor in hendrerit in vulputate velit esse molestie consequat, vel illum dolore</span>
        <span class="line">eu feugiat nulla facilisis at vero et accumsan et iusto odio dignissim qui</span>
        <span class="line">blandit praesent luptatum zzril delenit augue</span>
      </p>
      <p>
        <span class="line">duis dolore te feugait nulla facilisi. Lorem ipsum dolor sit amet, consectetuer</span>
        <span class="line">adipiscing elit, sed diam nonummy nibh euismod tincidunt ut laoreet dolore</span>
        <span class="line">magna aliquam erat volutpat. Ut wisi enim ad minim veniam, quis nostrud</span>
        <span class="line">exerci tation ullamcorper suscipit lobortis nisl ut aliquip ex ea commodo</span>
        <span class="line">consequat. Duis autem vel eum iriure dolor in hendrerit in vulputate velit</span>
        <span class="line">esse molestie consequat, vel illum dolore eu</span>
      </p>
      <p>
        <span class="line">feugiat nulla facilisis at vero et accumsan et iusto odio dignissim qui blandit</span>
        <span class="line">praesent luptatum zzril delenit augue duis dolore te feugait nulla facilisi.</span>
        <span class="line">Nam liber tempor cum soluta nobis eleifend option congue nihil imperdiet</span>
        <span class="line">doming id quod mazim placerat facer possim assum.</span>
      </p>
    </div>
  </section>

  <section class="spine">
    <svg width="55" height="601" viewBox="0 0 55 601">
      <g fill="#ffffff" font-family="Barlow, Arial, sans-serif" font-size="19" font-weight="400" letter-spacing="1">
        <text class="spine-title" transform="translate(39 207) rotate(-90)" textLength="117" lengthAdjust="spacingAndGlyphs">DEAL SPRINTS</text>
        <text class="spine-author" transform="translate(39 574) rotate(-90)" textLength="144" lengthAdjust="spacingAndGlyphs">TORSTEN WEHMEYER</text>
      </g>
    </svg>
  </section>

  <section class="front-cover">
    <svg width="425" height="320" viewBox="0 0 425 320">
      <g fill="#ffffff" font-family="Barlow, Arial, sans-serif" font-weight="700">
        <text class="front-title-top" x="27" y="165" font-size="116" textLength="364" lengthAdjust="spacingAndGlyphs">DEAL</text>
        <text class="front-title-bottom" x="27" y="282" font-size="116" textLength="364" lengthAdjust="spacingAndGlyphs">SPRINTS</text>
      </g>
      <rect class="subtitle-band" x="0" y="224" width="425" height="28" fill="#009fe3"/>
      <text class="subtitle" x="32" y="246" fill="#ffffff" font-family="Barlow, Arial, sans-serif" font-size="18" font-weight="400" textLength="359" lengthAdjust="spacingAndGlyphs">DER SCHUB FÜR IHRE VERHANDLUNGSSTÄRKE</text>
    </svg>
    <div class="cover-art" role="img" aria-label="Weiße Illustration zweier Hände beim Handschlag"></div>
    <p class="front-author">TORSTEN WEHMEYER</p>
  </section>

</div>
</body>
</html>
```